Physician House Call Doctor

I need 2 newspaper color display adds. 1 small and 1 larger. I have attached some ideas but they need to be updated, more professional and eye-catching . I may also want to change the doctors picture and add some text. I need submit to newspaper in a PDF format and the adds must have a border.

```html
<!DOCTYPE html>
<html lang="en">
<head>
<meta charset="utf-8">
<title>Physician House Calls – Display Ad</title>
<link href="https://fonts.googleapis.com/css2?family=Arimo:wght@400;700&family=Tinos&display=swap" rel="stylesheet">
<style>
  :root {
    --navy: #1b3f6e;
    --navy-deep: #163862;
    --blue: #2a7fc0;
    --blue-bright: #2f95d3;
    --sky: #3aa0dc;
    --ink: #1e3560;
    --link-blue: #2b86c6;
    --grey: #c9cbcd;
    --white: #ffffff;
    --page: #ececec;
  }
  * { box-sizing: border-box; margin: 0; padding: 0; }
  html, body { width: 988px; height: 1200px; overflow: hidden; background: var(--page); }
  .ad {
    position: relative; width: 988px; height: 1200px;
    background: var(--navy); font-family: "Arimo", Arial, sans-serif;
  }
  .ad__panel {
    position: absolute; left: 28px; top: 26px; width: 932px; height: 1148px;
    background: var(--white); overflow: hidden;
  }
  .ad__shapes { position: absolute; inset: 0; }
  .ad__map {
    position: absolute; left: 10px; top: 300px; width: 890px; height: 300px;
    background: radial-gradient(ellipse at center, rgba(225,229,233,.7), rgba(240,242,244,0) 70%);
  }
  .headline { position: absolute; left: 0; right: 0; text-align: center; color: var(--white); font-weight: 700; }
  .headline--title { top: 46px; font-size: 62px; letter-spacing: 1px; }
  .headline--sub { top: 132px; font-size: 47px; }
  .pitch { position: absolute; left: 0; right: 0; text-align: center; font-family: "Tinos", "Times New Roman", serif; }
  .pitch--lead { top: 307px; font-size: 30px; color: var(--ink); }
  .pitch--accent { font-size: 33px; color: var(--link-blue); }
  .pitch--a1 { top: 353px; }
  .pitch--a2 { top: 402px; }
  .benefits { position: absolute; left: 56px; top: 494px; list-style: none; color: var(--ink); font-size: 21px; line-height: 24px; }
  .benefits li { position: relative; padding-left: 26px; margin-bottom: 17px; }
  .benefits svg { position: absolute; left: 0; top: 4px; }
  .doctor-photo {
    position: absolute; left: 520px; top: 563px; width: 412px; height: 462px;
    background: linear-gradient(180deg, #e7e0dc 0%, #d9c6bd 30%, #f1f1f1 60%, #1e2630 100%);
    clip-path: ellipse(60% 62% at 60% 70%);
  }
  .house-photo {
    position: absolute; left: 0; top: 820px; width: 520px; height: 230px;
    background: linear-gradient(180deg, rgba(90,140,190,.35), rgba(40,110,175,0));
  }
  .brand { position: absolute; left: 127px; top: 846px; display: flex; align-items: center; gap: 10px; color: var(--white); font-size: 22px; font-weight: 700; }
  .brand__mark { width: 18px; height: 18px; background: var(--white); }
  .credentials { position: absolute; left: 127px; top: 904px; color: var(--white); font-size: 27px; line-height: 33px; }
  .credentials__name { font-weight: 700; font-size: 28px; }
  .call {
    position: absolute; left: 56px; top: 1027px; width: 807px; height: 76px;
    border-radius: 38px; background: var(--blue-bright);
    display: flex; align-items: center; justify-content: center; gap: 18px;
    color: var(--white); font-weight: 700; font-size: 68px;
  }
  .website { position: absolute; left: 0; right: 0; top: 1108px; text-align: center; color: var(--white); font-size: 25px; letter-spacing: 2px; }
</style>
</head>
<body>
<main class="ad">
  <section class="ad__panel">
    <svg class="ad__shapes" width="932" height="1148" viewBox="0 0 932 1148">
      <defs>
        <linearGradient id="headerFill" x1="0" y1="0" x2="1" y2="0.3">
          <stop offset="0" stop-color="#1c4478"/>
          <stop offset="1" stop-color="#2a93d2"/>
        </linearGradient>
        <linearGradient id="footerFill" x1="0" y1="0" x2="1" y2="0">
          <stop offset="0" stop-color="#23568f"/>
          <stop offset="1" stop-color="#2f86c8"/>
        </linearGradient>
      </defs>
      <path d="M0 0H932V203Q466 270 0 203Z" fill="url(#headerFill)"/>
      <path d="M0 203Q466 270 932 203V214Q466 285 0 214Z" fill="var(--grey)"/>
      <path d="M0 823Q400 740 932 790V1148H0Z" fill="url(#footerFill)"/>
      <path d="M0 823Q400 740 932 790V812Q400 758 0 840Z" fill="#b9bcbf"/>
      <path d="M620 790Q800 785 932 812V835Q800 805 640 808Z" fill="#151515"/>
    </svg>

    <div class="ad__map" role="img" aria-label="Faint world map background"></div>

    <h1 class="headline headline--title">PHYSICIAN HOUSE CALLS</h1>
    <p class="headline headline--sub">Affordable and Convenient</p>

    <p class="pitch pitch--lead">Can’t get to the doctor or your doctor can’t see you right away,</p>
    <p class="pitch pitch--accent pitch--a1">Dr. Holloway will come to you.</p>
    <p class="pitch pitch--accent pitch--a2">He is Maple Grove and the surrounding area!</p>

    <ul class="benefits">
      <li><svg width="19" height="19" viewBox="0 0 20 20"><circle cx="10" cy="10" r="8.5" fill="none" stroke="var(--ink)" stroke-width="1.6"/><path d="M6 10l3 3 5-6" fill="none" stroke="var(--ink)" stroke-width="1.8"/></svg>Medicare is accepted for qualified patients,<br>you pay a small trip fee for your house call.</li>
      <li><svg width="19" height="19" viewBox="0 0 20 20"><circle cx="10" cy="10" r="8.5" fill="none" stroke="var(--ink)" stroke-width="1.6"/><path d="M6 10l3 3 5-6" fill="none" stroke="var(--ink)" stroke-width="1.8"/></svg>Dr. Holloway does family consults, second opinions<br>medical testing and evaluations.</li>
      <li><svg width="19" height="19" viewBox="0 0 20 20"><circle cx="10" cy="10" r="8.5" fill="none" stroke="var(--ink)" stroke-width="1.6"/><path d="M6 10l3 3 5-6" fill="none" stroke="var(--ink)" stroke-width="1.8"/></svg>We also offer Lab Testing, X-rays Breathing Treatments<br>all in the comfort of your home.</li>
      <li><svg width="19" height="19" viewBox="0 0 20 20"><circle cx="10" cy="10" r="8.5" fill="none" stroke="var(--ink)" stroke-width="1.6"/><path d="M6 10l3 3 5-6" fill="none" stroke="var(--ink)" stroke-width="1.8"/></svg>Convenient Daytime Hours<br>Open most evenings, weekends, and holidays!</li>
    </ul>

    <div class="house-photo" role="img" aria-label="Faded photo of a suburban house"></div>
    <div class="doctor-photo" role="img" aria-label="Portrait of the doctor in a white coat with stethoscope"></div>

    <div class="brand"><span class="brand__mark"></span>Harbor Direct Care Medical</div>
    <div class="credentials">
      <p class="credentials__name">Daniel R. Holloway, MD</p>
      <p>Primary and Urgent Care</p>
      <p>Board Certified Family Medicine</p>
    </div>

    <div class="call">
      <span>CALL</span>
      <svg width="54" height="54" viewBox="0 0 54 54"><circle cx="27" cy="27" r="23" fill="none" stroke="var(--white)" stroke-width="5"/><path d="M19 15c2-1 4 0 5 3l1 3c0 2-2 3-2 4 1 3 4 6 7 7 1 0 2-2 4-2l3 1c3 1 4 3 3 5-1 3-4 4-7 3-8-2-14-8-16-16-1-4 0-7 2-8z" fill="var(--white)"/></svg>
      <span>202-555-0148</span>
    </div>
    <p class="website">www.harbordcmed.com</p>
  </section>
</main>
</body>
</html>
```